Kelvo Car Audio - Stationary Needed
Business Card, Letterhead, Envelope, Fax Cover, E-mail Signature
Kelvo Car Audio - Stationary Needed -
Creative Brief
Use specific fonts
Designers discretion
Professional
Marcus Feltin
President / CEO
4182 W. Linden Ave. Santa Ana, CA 92817
marc@kelvocaraudio.example
www.kelvocaraudio.example
For business card, use Black background w/ White font.
Would like map of our location, along with the following services we offer: - Car Audio Sales and Installation - Remote Start / Vehicle Security - GPS Navigation - Smartphone/Wireless Integration - Custom and Pre-Fab Enclosures - Professional Window Tint

```html
<!DOCTYPE html>
<html lang="en">
<head>
<meta charset="utf-8">
<title>Kelvo Car Audio — Stationery Set</title>
<link rel="stylesheet" href="https://fonts.googleapis.com/css2?family=Rajdhani:wght@500;700&family=Open+Sans:wght@400;600&display=swap">
<style>
  :root {
    --ink: #0d0d0f;
    --panel: #16171a;
    --paper: #ffffff;
    --board: #ffffff;
    --accent: #2f86c8;
    --muted: #8a8d92;
    --rule: #c9cbcf;
    --body: #4a4c50;
    --map-a: #3a3d42;
    --map-b: #25272b;
  }
  * { box-sizing: border-box; margin: 0; padding: 0; }
  html, body { width: 1200px; height: 492px; overflow: hidden; background: var(--board); }
  body { position: relative; font-family: "Open Sans", sans-serif; color: var(--body); }

  .sheet { position: absolute; background: var(--paper); box-shadow: 0 1px 3px rgba(0,0,0,.28); overflow: hidden; }
  .brand { font-family: "Rajdhani", sans-serif; font-weight: 700; letter-spacing: .04em; text-transform: uppercase; color: #fff; line-height: 1; }
  .tagline { font-family: "Rajdhani", sans-serif; font-weight: 500; font-size: 4.5px; letter-spacing: .12em; text-transform: uppercase; color: var(--muted); margin-top: 2px; }

  .sheet-header { height: 52px; background: var(--ink); display: flex; justify-content: space-between; align-items: center; padding: 0 14px; }
  .sheet-header .brand { font-size: 13px; }
  .header-contact { text-align: right; font-size: 4.2px; line-height: 1.5; color: #d7d9dc; }
  .header-contact strong { font-size: 5.5px; color: #fff; font-weight: 600; }
  .sheet-footer { position: absolute; left: 0; right: 0; bottom: 0; height: 26px; background: var(--ink); display: flex; flex-direction: column; align-items: center; justify-content: center; }
  .sheet-footer .brand { font-size: 7px; }
  .sheet-footer .web { font-size: 3.6px; color: var(--muted); margin-top: 2px; }

  .copy { padding: 0 18px; font-size: 4.3px; line-height: 1.6; }
  .copy p { margin-bottom: 5px; }

  .fax { left: 12px; top: 25px; width: 313px; height: 437px; }
  .fax-fields { display: grid; grid-template-columns: 1fr 1fr; column-gap: 26px; row-gap: 7px; padding: 16px 18px 10px; }
  .field { display: flex; align-items: flex-end; font-size: 4.6px; font-weight: 600; color: var(--ink); }
  .field span { flex: 1; border-bottom: .6px solid var(--rule); margin-left: 5px; height: 5px; }
  .fax-checks { display: flex; gap: 11px; padding: 4px 18px 12px; font-size: 4.3px; }
  .fax-checks span::before { content: ""; display: inline-block; width: 4px; height: 4px; border: .6px solid var(--ink); margin-right: 2px; vertical-align: -0.5px; }
  .message-label { padding: 0 18px 6px; font-size: 5px; font-weight: 600; color: var(--ink); }
  .signoff { text-align: right; }

  .letterhead { left: 350px; top: 25px; width: 313px; height: 437px; }
  .letterhead .copy { padding-top: 28px; }

  .card { position: absolute; width: 162px; height: 100px; background: var(--ink); box-shadow: 0 1px 3px rgba(0,0,0,.3); color: #fff; }
  .card-front { left: 688px; top: 48px; }
  .card-front .card-top { height: 36px; background: var(--panel); display: flex; align-items: center; justify-content: center; }
  .card-front .brand { font-size: 11px; }
  .card-front .card-id { text-align: center; padding-top: 14px; }
  .card-name { font-family: "Rajdhani", sans-serif; font-weight: 700; font-size: 7px; letter-spacing: .06em; text-transform: uppercase; }
  .card-role { font-size: 4px; color: var(--muted); margin-top: 1px; }
  .card-lines { font-size: 3.8px; line-height: 1.5; color: #cfd1d4; margin-top: 6px; }

  .card-back { left: 862px; top: 100px; display: flex; padding: 10px; gap: 8px; }
  .map { width: 62px; height: 80px; background: linear-gradient(135deg, var(--map-a), var(--map-b)); border: .6px solid #4a4d52; }
  .services { flex: 1; font-size: 3.7px; line-height: 1.55; color: #d4d6d9; }
  .services h3 { font-family: "Rajdhani", sans-serif; font-size: 5.5px; font-weight: 700; text-transform: uppercase; letter-spacing: .08em; color: #fff; margin-bottom: 3px; }
  .services li { list-style: none; }
  .services li::before { content: "›"; color: var(--accent); margin-right: 2px; }

  .email-sig { position: absolute; left: 1048px; top: 98px; width: 148px; display: flex; align-items: center; gap: 6px; }
  .email-sig .mark { display: flex; flex-direction: column; }
  .email-sig .brand { color: var(--accent); font-size: 11.5px; line-height: .95; width: 70px; }
  .email-sig .divider { width: .8px; align-self: stretch; background: var(--accent); }
  .email-sig .sig-lines { font-size: 3.8px; line-height: 1.55; color: var(--muted); }
  .email-sig .sig-lines strong { color: var(--ink); font-size: 4.4px; }

  .envelope { left: 688px; top: 262px; width: 350px; height: 175px; }
  .env-band { position: absolute; left: 0; top: 0; bottom: 0; width: 84px; background: var(--ink); padding: 12px 9px; color: #fff; }
  .env-band .card-name { font-size: 6px; }
  .env-band .card-role { font-size: 3.6px; }
  .env-band .return { font-size: 3.6px; line-height: 1.5; color: #cfd1d4; margin-top: 4px; }
  .env-band .brand { position: absolute; left: 9px; bottom: 12px; font-size: 8px; }
  .env-mark { position: absolute; left: 150px; top: 48px; width: 150px; height: 80px; border-radius: 50%; background: radial-gradient(ellipse at center, #eef0f2, #fff 70%); }

  .label { position: absolute; left: 1050px; top: 372px; width: 145px; height: 40px; background: var(--ink); box-shadow: 0 1px 3px rgba(0,0,0,.3); display: flex; flex-direction: column; justify-content: center; align-items: flex-end; padding-right: 10px; color: #fff; }
  .label .card-name { font-size: 6.5px; }
  .label .card-role { font-size: 3.6px; }
</style>
</head>
<body>

<section class="sheet fax" aria-label="Fax cover sheet">
  <header class="sheet-header">
    <div><div class="brand">Kelvo Car Audio</div><div class="tagline">Premium Car Audio &amp; Installation</div></div>
    <div class="header-contact"><strong>Marcus Feltin</strong><br>President / CEO<br>4182 W. Linden Ave. Santa Ana, CA 92817<br>(714) 555-0148<br>marc@kelvocaraudio.example</div>
  </header>
  <div class="fax-fields">
    <div class="field">To:<span></span></div><div class="field">From:<span></span></div>
    <div class="field">Fax:<span></span></div><div class="field">Phone:<span></span></div>
    <div class="field">Pages:<span></span></div><div class="field">Date:<span></span></div>
    <div class="field">Re:<span></span></div><div class="field">CC:<span></span></div>
  </div>
  <div class="fax-checks"><span>Urgent</span><span>For Review</span><span>Please Comment</span><span>Please Reply</span><span>Recycle</span></div>
  <div class="message-label">Message:</div>
  <div class="copy">
    <p>Dear Customer,</p>
    <p>Thank you for choosing our shop for your vehicle sound system. This cover sheet accompanies the quote and installation schedule we discussed. Please review each page and confirm the options you would like us to order before your appointment.</p>
    <p>Our team handles remote start, security, navigation and custom enclosures in house. If anything on the attached pages is unclear, call or email us and we will walk through it with you.</p>
    <p class="signoff">Sincerely,<br>Marcus Feltin</p>
  </div>
  <footer class="sheet-footer"><div class="brand">Kelvo Car Audio</div><div class="web">www.kelvocaraudio.example</div></footer>
</section>

<section class="sheet letterhead" aria-label="Letterhead">
  <header class="sheet-header">
    <div><div class="brand">Kelvo Car Audio</div><div class="tagline">Premium Car Audio &amp; Installation</div></div>
    <div class="header-contact"><strong>Marcus Feltin</strong><br>President / CEO<br>4182 W. Linden Ave. Santa Ana, CA 92817<br>(714) 555-0148<br>marc@kelvocaraudio.example</div>
  </header>
  <div class="copy">
    <p>Dear Customer,</p>
    <p>Thank you for choosing our shop for your vehicle sound system. This letter follows up on the quote and installation schedule we discussed. Please review the details and confirm the options you would like us to order before your appointment.</p>
    <p>Our team handles remote start, security, navigation and custom enclosures in house. If anything in this letter is unclear, call or email us and we will walk through it with you.</p>
    <p>We look forward to working on your vehicle and appreciate your business.</p>
    <p class="signoff">Sincerely,<br>Marcus Feltin</p>
  </div>
  <footer class="sheet-footer"><div class="brand">Kelvo Car Audio</div><div class="web">www.kelvocaraudio.example</div></footer>
</section>

<article class="card card-front" aria-label="Business card front">
  <div class="card-top"><div class="brand">Kelvo Car Audio</div></div>
  <div class="card-id">
    <div class="card-name">Marcus Feltin</div>
    <div class="card-role">President / CEO</div>
    <div class="card-lines">4182 W. Linden Ave. Santa Ana, CA 92817<br>(714) 555-0148 · marc@kelvocaraudio.example<br>www.kelvocaraudio.example</div>
  </div>
</article>

<article class="card card-back" aria-label="Business card back">
  <div class="map" role="img" aria-label="Map showing the shop location"></div>
  <div class="services">
    <h3>Services</h3>
    <ul>
      <li>Car Audio Sales and Installation</li>
      <li>Remote Start / Vehicle Security</li>
      <li>GPS Navigation</li>
      <li>Smartphone/Wireless Integration</li>
      <li>Custom and Pre-Fab Enclosures</li>
      <li>Professional Window Tint</li>
    </ul>
  </div>
</article>

<aside class="email-sig" aria-label="E-mail signature">
  <div class="mark"><div class="brand">Kelvo Car Audio</div><div class="tagline">Premium Car Audio &amp; Installation</div></div>
  <div class="divider"></div>
  <div class="sig-lines"><strong>Marcus Feltin</strong><br>President / CEO<br>(714) 555-0148<br>marc@kelvocaraudio.example<br>www.kelvocaraudio.example</div>
</aside>

<section class="sheet envelope" aria-label="Envelope">
  <div class="env-band">
    <div class="card-name">Marcus Feltin</div>
    <div class="card-role">President / CEO</div>
    <div class="return">4182 W. Linden Ave.<br>Santa Ana, CA 92817</div>
    <div class="brand">Kelvo Car Audio</div>
  </div>
  <div class="env-mark"></div>
</section>

<div class="label" aria-label="Mailing label">
  <div class="card-name">Marcus Feltin</div>
  <div class="card-role">President / CEO</div>
</div>

</body>
</html>
```